Willow Dental Business Card

We need business cards for our dental office.
We are looking for a clean, elegant design

We provide dental services to children.
Our card needs to be appealing to referring dentists, parents and our team

Target Market(s)

referring dentists, parents and our team

Industry/Entity Type

Dental Clinic

Contact Information for Business Card

4856 Fenwick Lane, Suite 100
Middleburg Heights, OH 44187

216-382-7461 Voice
216-382-7469 fax
info@willowdentalco.com email
www.willowdentalco.com web

Font styles to use
Sans Serif

Requirements
Must have
• White background - clean, crisp, elegant, simple
• rounded corners
• different color palate - once we come up with design, we will replace the blue with orange, green,
Nice to have
• Follow our logo typeface and colors
• then we can replace color

```html
<!DOCTYPE html>
<html lang="en">
<head>
<meta charset="utf-8">
<title>Willow Dental Business Card</title>
<link rel="stylesheet" href="https://fonts.googleapis.com/css2?family=Poppins:wght@400;500;600&family=Roboto:wght@400&display=swap">
<style>
  :root {
    --page-bg: #1f1f1f;
    --card-white: #ffffff;
    --brand-blue: #00aeef;
    --text-white: #ffffff;
    --back-grey-top: #b2b4b6;
    --back-grey-bottom: #a4a6a9;
  }
  * { box-sizing: border-box; margin: 0; padding: 0; }
  html, body {
    width: 1200px; height: 1200px; overflow: hidden;
    background: var(--page-bg);
  }
  .card {
    position: absolute;
    left: 262px;
    width: 800px; height: 457px;
    transform: scale(0.8575);
    transform-origin: top left;
    border-radius: 26px;
    overflow: hidden;
    font-family: "Poppins", sans-serif;
  }
  .card-front { top: 165px; background: var(--card-white); }
  .card-back {
    top: 653px;
    background: linear-gradient(180deg, var(--back-grey-top), var(--back-grey-bottom));
  }
  .front-wave { position: absolute; inset: 0; width: 100%; height: 100%; }
  .brand-name {
    position: absolute; left: 64px; top: 142px;
    font-size: 44px; font-weight: 500; color: var(--brand-blue);
    letter-spacing: -0.5px; white-space: nowrap;
  }
  .holder {
    position: absolute; right: 40px; top: 262px; text-align: right;
    color: var(--text-white);
  }
  .holder-name { font-size: 31px; font-weight: 600; line-height: 1.1; }
  .holder-title { font-size: 22px; font-weight: 500; line-height: 1.3; }
  .contact-list {
    position: absolute; right: 40px; top: 336px; list-style: none;
    color: var(--text-white); font-size: 19px; line-height: 24.5px;
  }
  .contact-list li {
    display: flex; justify-content: flex-end; align-items: center; gap: 12px;
  }
  .contact-list svg { width: 19px; height: 19px; flex: none; }
  .address {
    position: absolute; left: 38px; top: 359px;
    color: var(--text-white); font-size: 19px; line-height: 24.5px;
    font-style: normal;
  }
  .back-brand {
    position: absolute; left: 0; right: 0; top: 160px; text-align: center;
    font-size: 66px; font-weight: 500; color: var(--text-white);
  }
  .back-url {
    position: absolute; left: 0; right: 0; top: 382px; text-align: center;
    font-family: "Roboto", sans-serif; font-size: 19px; letter-spacing: 4px;
    color: var(--text-white);
  }
</style>
</head>
<body>
  <section class="card card-front">
    <svg class="front-wave" viewBox="0 0 800 457" preserveAspectRatio="none" aria-hidden="true">
      <path d="M0 270 C80 310 180 318 330 290 C480 262 620 222 700 222 C750 222 780 240 800 262 L800 457 L0 457 Z" fill="var(--brand-blue)"/>
      <path d="M0 262 C80 292 170 300 320 275 C470 250 600 212 680 210 C740 208 780 228 800 258" fill="none" stroke="var(--brand-blue)" stroke-width="6"/>
    </svg>
    <div class="brand-name">Willow Dental</div>
    <div class="holder">
      <div class="holder-name">Daniel Mercer</div>
      <div class="holder-title">Founder &amp; CEO</div>
    </div>
    <address class="address">
      4856 Fenwick Lane<br>
      Suite 100, Middleburg<br>
      Heights, OH 44187
    </address>
    <ul class="contact-list">
      <li>216-382-7461
        <svg viewBox="0 0 24 24" aria-label="Phone"><path fill="currentColor" d="M6.6 10.8a15 15 0 0 0 6.6 6.6l2.2-2.2c.3-.3.7-.4 1-.2 1.1.4 2.3.6 3.6.6.6 0 1 .4 1 1V20c0 .6-.4 1-1 1A17 17 0 0 1 3 4c0-.6.4-1 1-1h3.5c.6 0 1 .4 1 1 0 1.3.2 2.5.6 3.6.1.3 0 .7-.2 1z"/></svg>
      </li>
      <li>216-382-7469
        <svg viewBox="0 0 24 24" aria-label="Fax"><path fill="currentColor" d="M7 3h8l2 2v4H7zM3 10h18v8h-3v3H6v-3H3zm5 6v3h8v-3z"/></svg>
      </li>
      <li>info@willowdentalco.com
        <svg viewBox="0 0 24 24" aria-label="Email"><path fill="currentColor" d="M3 5h18v14H3zm2 2v.5l7 5 7-5V7zm0 3v7h14v-7l-7 5z"/></svg>
      </li>
      <li>www.willowdentalco.com
        <svg viewBox="0 0 24 24" aria-label="Website"><circle cx="12" cy="12" r="9" fill="currentColor"/><path d="M3 12h18M12 3c3 3 3 15 0 18M12 3c-3 3-3 15 0 18" stroke="var(--brand-blue)" stroke-width="1.5" fill="none"/></svg>
      </li>
    </ul>
  </section>

  <section class="card card-back">
    <div class="back-brand">Willow Dental</div>
    <div class="back-url">www.willowdentalco.com</div>
  </section>
</body>
</html>
```